Amber Ridge Productions

I need a business card design for a new freelance film production company using or incorporating the logo:
I want the card to be creative, minimal, yet professional. Feel free to use a variety of different shapes and sizes/ textures for the card.

Industry/Entity Type

Film Production

```html
<!DOCTYPE html>
<html lang="en">
<head>
<meta charset="UTF-8">
<title>Amber Ridge Productions – Business Card</title>
<link rel="stylesheet" href="https://fonts.googleapis.com/css2?family=Jost:wght@400;500;600&display=swap">
<style>
  :root {
    --backdrop: #dedede;
    --card-white: #ffffff;
    --brand-blue: #0f54a3;
    --ink-white: #ffffff;
    --divider-white: #f4f4f4;
    --shadow: rgba(0, 0, 0, 0.28);
  }
  * { margin: 0; padding: 0; box-sizing: border-box; }
  html, body {
    width: 1200px;
    height: 1200px;
    overflow: hidden;
    background: var(--backdrop);
    font-family: "Jost", "Futura", sans-serif;
  }
  .canvas {
    position: relative;
    width: 1200px;
    height: 1200px;
  }
  .card {
    position: absolute;
    box-shadow: 0 14px 26px var(--shadow);
  }
  /* Front: white with logo */
  .card-front {
    left: 90px;
    top: 300px;
    width: 560px;
    height: 320px;
    background: var(--card-white);
  }
  .card-front .divider {
    position: absolute;
    left: 279px;
    top: 0;
    width: 4px;
    height: 100%;
    background: var(--brand-blue);
  }
  .wordmark {
    position: absolute;
    left: 32px;
    bottom: 22px;
    display: flex;
    align-items: flex-end;
    gap: 10px;
    color: var(--brand-blue);
    font-weight: 500;
  }
  .wordmark-square {
    width: 26px;
    height: 26px;
    background: var(--brand-blue);
    margin-bottom: 4px;
  }
  .wordmark-text {
    display: flex;
    flex-direction: column;
    line-height: 1;
  }
  .wordmark-name {
    font-size: 27px;
    letter-spacing: 0.5px;
  }
  .wordmark-sub {
    font-size: 10px;
    letter-spacing: 5px;
    margin-top: 5px;
  }
  /* Back: blue with contact details */
  .card-back {
    left: 510px;
    top: 430px;
    width: 610px;
    height: 348px;
    background: var(--brand-blue);
    color: var(--ink-white);
  }
  .card-back .divider {
    position: absolute;
    left: 303px;
    top: 0;
    width: 4px;
    height: 100%;
    background: var(--divider-white);
  }
  .contact {
    position: absolute;
    right: 22px;
    top: 0;
    bottom: 0;
    width: 270px;
    text-align: right;
  }
  .person-name {
    position: absolute;
    right: 0;
    top: 190px;
    font-size: 24px;
    font-weight: 600;
    letter-spacing: 0.5px;
    line-height: 1;
  }
  .person-role {
    position: absolute;
    right: 0;
    top: 217px;
    font-size: 15px;
    font-style: italic;
    font-weight: 400;
    line-height: 1;
  }
  .contact-lines {
    position: absolute;
    right: 0;
    top: 250px;
    font-size: 17px;
    line-height: 1.35;
  }
  .website {
    position: absolute;
    right: 0;
    bottom: 14px;
    font-size: 17px;
    letter-spacing: 3px;
  }
</style>
</head>
<body>
  <main class="canvas">
    <section class="card card-front">
      <div class="wordmark">
        <span class="wordmark-square"></span>
        <span class="wordmark-text">
          <span class="wordmark-name">AMBER RIDGE</span>
          <span class="wordmark-sub">PRODUCTIONS</span>
        </span>
      </div>
      <div class="divider"></div>
    </section>

    <section class="card card-back">
      <div class="divider"></div>
      <div class="contact">
        <p class="person-name">MARA QUINN</p>
        <p class="person-role">Founder</p>
        <p class="contact-lines">888.512.7730<br>mara@amberridge.com</p>
        <p class="website">www.amberridge.com</p>
      </div>
    </section>
  </main>
</body>
</html>
```